CD Cover für junge Pop-Rock Band
Sehr kreative vorschläge. mehrere designs, die alle unter den top-favoriten für uns waren. änderungen und anpassungen stets schnell umgesetzt und auch nach gewinner-auswahl noch weiter zusammen gearbeitet bevor das endgültige design übergeben wurde.
Zielgruppe
Wir sind eine junge Band aus München und machen ausschließlich eigene Songs im Bereich Pop-Rock. Durch Einflüsse aus verschiedenen anderen Genres wie Funk, Reggae und Britpop grenzen sich unsere Songs von typischem Mainstream-Pop ab. Unsere Zielgruppe setzt sich aus Personen verschiedener Altersgruppen zusammen, der Fokus liegt jedoch auf Mitte Zwanzig- bis Mitte Dreißig-Jährigen.
Homepage: www.velvetmorrow.com
Chatterloop: www.chatterloop.net/velvetmorrowband
Aufgabenstellung
Wir benötigen ein Design für unsere neue EP "Paper Rivers". Diese wird in Form eines DigiPacks veröffentlicht werden. Daher werden Designs für Vorderseite, Rückseite, zwei Innenseiten sowie die CD selbst benötigt.
Folgendes sollte auf den jeweiligen Seiten enthalten sein:
Vorderseite:
- Bandschriftzug (siehe Anhang)
- Name der EP: Paper Rivers
Rückseite:
- Trackliste (1.Copper Kite, 2.Hold Us Near, 3.Birch Alley, 4.Can We Stay, 5.Quiet Hours)
- Credits (Recording by ..., Mix by ..., Mastering by ..., etc. -> wird noch festgesetzt)
Anmerkung:
Die roten Kratzer aus dem Bandlogo können bei Bedarf frei verwendet werden hinsichtlich Farbe, Muster, Gestaltung, Größe, etc.
Wir möchten keine Bilder von uns (z.B. von unserer Homepage, Chatterloop, etc) auf der CD.

```html
<!DOCTYPE html>
<html lang="en">
<head>
<meta charset="utf-8">
<title>Velvet Morrow – Paper Rivers</title>
<link href="https://fonts.googleapis.com/css2?family=Montserrat:wght@300;400&display=swap" rel="stylesheet">
<style>
  :root {
    --backdrop: #eef0f1;
    --night: #141414;
    --ink: #2a2a2a;
    --paper: #ffffff;
    --mist: #e4e4e4;
    --amber: #b8651e;
    --accent: #c4161c;
  }
  html, body {
    margin: 0;
    width: 1200px;
    height: 809px;
    overflow: hidden;
    background: var(--backdrop);
    font-family: "Montserrat", Arial, sans-serif;
  }
  .booklet {
    position: absolute;
    left: 55px;
    top: 171px;
    display: flex;
    gap: 30px;
  }
  .panel {
    position: relative;
    width: 530px;
    height: 466px;
    overflow: hidden;
  }
  .cover-front {
    background: var(--night);
  }
  .cover-photo {
    position: absolute;
    inset: 0;
    background:
      radial-gradient(ellipse 55% 45% at 30% 68%, rgba(184,101,30,0.85), rgba(120,60,20,0.4) 55%, transparent 80%),
      linear-gradient(160deg, #1c1c1c 0%, #0d0d0d 60%, #161310 100%);
  }
  .band-name {
    font-weight: 300;
    letter-spacing: 0.04em;
    text-transform: uppercase;
    white-space: nowrap;
  }
  .cover-front .band-name {
    position: absolute;
    right: 28px;
    bottom: 40px;
    font-size: 20px;
    color: var(--paper);
    display: flex;
    align-items: center;
    gap: 8px;
  }
  .band-mark {
    width: 12px;
    height: 12px;
    background: var(--accent);
  }
  .inlay {
    background: var(--paper);
  }
  .inlay-photo {
    position: absolute;
    top: 0;
    right: 0;
    width: 300px;
    height: 100%;
    background: linear-gradient(90deg, rgba(255,255,255,1) 0%, rgba(210,210,210,0.6) 40%, var(--mist) 100%);
  }
  .inlay .band-name {
    position: absolute;
    left: 14px;
    top: 22px;
    writing-mode: vertical-rl;
    transform: rotate(180deg);
    font-size: 44px;
    color: var(--ink);
  }
  .disc {
    position: absolute;
    left: 63px;
    top: 13px;
    width: 440px;
    height: 440px;
  }
  .disc-title {
    font-family: "Montserrat", Arial, sans-serif;
    font-weight: 300;
    font-size: 30px;
    letter-spacing: 0.03em;
    fill: var(--paper);
  }
  .disc-band {
    font-family: "Montserrat", Arial, sans-serif;
    font-weight: 300;
    font-size: 15px;
    letter-spacing: 0.04em;
    fill: var(--paper);
  }
</style>
</head>
<body>
  <main class="booklet">
    <section class="panel cover-front">
      <div class="cover-photo" role="img" aria-label="Close-up photo of a hand playing an amber electric bass guitar on a dark background"></div>
      <div class="band-name"><span class="band-mark"></span>Velvet Morrow</div>
    </section>

    <section class="panel inlay">
      <div class="inlay-photo" role="img" aria-label="Faded black and white photo of a musician behind a drum kit"></div>
      <div class="band-name">Velvet Morrow</div>
      <svg class="disc" viewBox="0 0 440 440" aria-label="CD disc">
        <defs>
          <radialGradient id="discFace" cx="50%" cy="55%" r="60%">
            <stop offset="0%" stop-color="#3a3a3a"/>
            <stop offset="70%" stop-color="#1e1e1e"/>
            <stop offset="100%" stop-color="#121212"/>
          </radialGradient>
        </defs>
        <circle cx="220" cy="220" r="216" fill="url(#discFace)" stroke="#ffffff" stroke-width="6"/>
        <circle cx="220" cy="220" r="70" fill="none" stroke="#ffffff" stroke-width="3"/>
        <circle cx="220" cy="220" r="20" fill="#ffffff"/>
        <text class="disc-title" x="220" y="118" text-anchor="middle">PAPER RIVERS</text>
        <rect x="150" y="324" width="10" height="10" fill="var(--accent)"/>
        <text class="disc-band" x="166" y="334">VELVET MORROW</text>
      </svg>
    </section>
  </main>
</body>
</html>
```